Help create retail shipping website

We need a Squarespace design for our company Tandem Parcel. We are a retail shipping service that offers mailboxes, shipping, notary, and printing services. This store is similar to a KWB store, BoxVane, and Ridgeway Mailhouse. We would like to have help designing our website. I will provide our logo for the website. I would like our website to be professional, but be very inviting.

```html
<!DOCTYPE html>
<html lang="en">
<head>
<meta charset="utf-8">
<title>Tandem Parcel</title>
<link href="https://fonts.googleapis.com/css2?family=Montserrat:wght@400;500;600;700;800&family=Lato:wght@400;700&family=Open+Sans:wght@800&display=swap" rel="stylesheet">
<style>
:root{
  --red:#e3140f;
  --black:#000;
  --ink:#111;
  --text:#333;
  --muted:#555;
  --grey:#efefef;
  --white:#fff;
}
*{box-sizing:border-box;margin:0;padding:0}
html,body{width:1200px;height:5119px;overflow:hidden;background:var(--white)}
body{font-family:'Lato',sans-serif;color:var(--text);position:relative}
.abs{position:absolute}
.center{text-align:center}
.btn{position:absolute;display:flex;align-items:center;justify-content:center;background:var(--red);color:var(--white);font-family:'Montserrat',sans-serif;font-weight:700;font-size:16px;letter-spacing:.5px;text-decoration:none}
.red{color:var(--red)}
.h2{font-family:'Montserrat',sans-serif;font-weight:700;font-size:50px;color:var(--ink);letter-spacing:.5px;left:0;width:1200px;text-align:center}

/* hero */
.hero{top:0;left:0;width:1200px;height:775px;background:linear-gradient(120deg,#6b5236 0%,#9a7851 35%,#3d3a3a 60%,#b28a5f 100%)}
.hero-shade{position:absolute;inset:0;background:linear-gradient(90deg,rgba(0,0,0,.45),rgba(0,0,0,.05))}
.brand{display:flex;align-items:center;gap:12px}
.brand-mark{width:24px;height:24px;background:var(--red);border-radius:50%}
.brand-name{font-family:'Montserrat',sans-serif;font-weight:800;font-size:24px;color:var(--white)}
.nav{top:68px;left:419px;display:flex;gap:0;font-family:'Montserrat',sans-serif;font-size:14px;color:var(--white);font-weight:500}
.nav a{color:var(--white);text-decoration:none;position:absolute;white-space:nowrap}
.hero-title{top:515px;left:74px;font-family:'Open Sans',sans-serif;font-weight:800;font-size:92px;color:var(--white);letter-spacing:1px}
.hero-sub{top:614px;left:76px;width:850px;font-size:29px;line-height:40px;color:var(--white)}

/* welcome */
.body-copy{font-size:17px;line-height:33px;color:var(--text)}

/* history */
.photo{border-radius:0}
.h-side{font-family:'Montserrat',sans-serif;font-weight:700;font-size:50px;color:var(--ink)}

/* services */
.services{top:1814px;left:0;width:1200px;height:656px;background:var(--black)}
.svc{position:absolute;top:0;width:270px;text-align:center;color:var(--white)}
.svc-icon{width:96px;height:96px;margin:0 auto;border-radius:8px}
.svc-title{margin-top:30px;font-family:'Montserrat',sans-serif;font-weight:700;font-size:20px}
.svc-text{margin-top:16px;font-size:16px;line-height:28px;padding:0 16px}

/* team */
.member{position:absolute;top:2633px;width:241px;text-align:center}
.member .ph{height:271px;background:linear-gradient(160deg,#d8dadc,#8e949a)}
.member .nm{margin-top:34px;font-family:'Montserrat',sans-serif;font-size:20px;color:var(--ink)}

/* quote */
.quote{top:3195px;left:0;width:1200px;height:477px;background:var(--grey)}
.quote p{position:absolute;top:96px;left:170px;width:860px;text-align:center;font-size:40px;line-height:57px;color:#222;font-family:'Lato',sans-serif}
.quote .who{position:absolute;top:345px;left:0;width:1200px;text-align:center;font-family:'Montserrat',sans-serif;font-size:22px;color:var(--red)}

/* blogs */
.post{position:absolute;top:3823px;width:331px;text-align:center}
.post .ph{height:252px}
.post .tt{margin-top:26px;font-family:'Montserrat',sans-serif;font-size:20px;line-height:34px;color:var(--ink)}
.post .more{display:block;margin-top:20px;font-family:'Montserrat',sans-serif;font-size:20px;color:var(--red);text-decoration:none}

/* cta */
.cta{top:4312px;left:0;width:1200px;height:409px;background:linear-gradient(100deg,#f0130d 0%,#b00808 45%,#1a0000 100%)}
.cta h2{position:absolute;top:78px;left:0;width:1200px;text-align:center;font-family:'Montserrat',sans-serif;font-weight:700;font-size:50px;line-height:60px;color:var(--white);letter-spacing:1px}
.cta .btn{top:248px;left:497px;width:207px;height:62px;background:transparent;border:2px solid var(--white)}

/* footer */
.foot{font-size:16px;color:var(--muted)}
.foot-h{font-family:'Montserrat',sans-serif;font-weight:600;font-size:22px;color:var(--ink)}
.foot-link{position:absolute;font-family:'Montserrat',sans-serif;font-size:15px;color:#444;text-decoration:none}
.social{top:4980px;left:448px;display:flex;gap:22px}
.social span{width:24px;height:24px;border-radius:50%;background:var(--ink)}
</style>
</head>
<body>

<header class="hero abs" role="img" aria-label="Photo of two colleagues reviewing a tablet in a warehouse stacked with cardboard boxes">
  <div class="hero-shade"></div>
</header>
<div class="abs brand" style="top:58px;left:76px">
  <span class="brand-mark"></span><span class="brand-name">TANDEMPARCEL</span>
</div>
<nav class="nav abs">
  <a href="#" style="left:0">ABOUT</a>
  <a href="#" style="left:90px">SERVICES</a>
  <a href="#" style="left:197px">TEAM</a>
  <a href="#" style="left:277px">BLOG</a>
</nav>
<a class="btn" href="#" style="top:44px;left:944px;width:183px;height:65px">CONTACT US</a>
<h1 class="abs hero-title">TANDEMPARCEL</h1>
<p class="abs hero-sub">We are a retail shipping service that offers mailboxes, shipping, notary, and printing services.</p>

<!-- welcome -->
<h2 class="abs h2" style="top:850px">WELCOME TO <span class="red">TANDEM</span> PARCEL</h2>
<p class="abs body-copy center" style="top:930px;left:120px;width:960px">Sed ut perspiciatis unde omnis iste natus error sit voluptatem accusantium doloremque laudantium, totam rem aperiam, eaque ipsa quae ab illo inventore veritatis et quasi architecto beatae vitae dicta sunt explicabo. Nemo enim ipsam voluptatem quia voluptas sit aspernatur aut odit aut fugit, sed quia consequuntur magni dolores eos qui ratione voluptatem sequi nesciunt.</p>
<a class="btn" href="#" style="top:1103px;left:497px;width:207px;height:65px">READ MORE</a>

<!-- history -->
<div class="abs photo" style="top:1274px;left:76px;width:512px;height:441px;background:linear-gradient(150deg,#e6e9ec,#a9b0b8)" role="img" aria-label="Photo of two colleagues reviewing documents at a laptop in a bright office"></div>
<h2 class="abs h-side" style="top:1380px;left:614px">COMPANY <span class="red">HISTORY</span></h2>
<p class="abs body-copy" style="top:1464px;left:614px;width:530px">Sed ut perspiciatis unde omnis iste natus error sit voluptatem accusantium doloremque laudantium, totam rem aperiam, eaque ipsa quae ab illo inventore veritatis et quasi architecto beatae vitae dicta sunt explicabo magni.</p>

<!-- services -->
<section class="services abs">
  <h2 class="abs" style="top:72px;left:0;width:1200px;text-align:center;font-family:'Montserrat',sans-serif;font-weight:700;font-size:50px;color:var(--white)">OUR SERVICES</h2>
  <div class="abs" style="top:167px;left:0;width:1200px;height:300px">
    <div class="svc" style="left:60px"><div class="svc-icon" style="background:#e45a3a" role="img" aria-label="Mailbox icon"></div><div class="svc-title">MAILBOXES</div><div class="svc-text">Sed ut perspiciatis unde omnis iste natus error sit luptatem accusantium dol oremque laudan</div></div>
    <div class="svc" style="left:330px"><div class="svc-icon" style="background:#f6c342" role="img" aria-label="Delivery truck icon"></div><div class="svc-title">SHIPPING</div><div class="svc-text">Sed ut perspiciatis unde omnis iste natus error sit luptatem accusantium dol oremque laudan</div></div>
    <div class="svc" style="left:600px"><div class="svc-icon" style="background:#1f7a86" role="img" aria-label="Fax and printer icon"></div><div class="svc-title">NOTARY</div><div class="svc-text">Sed ut perspiciatis unde omnis iste natus error sit luptatem accusantium dol oremque laudan</div></div>
    <div class="svc" style="left:870px"><div class="svc-icon" style="background:#e9e3d6" role="img" aria-label="Stamped document icon"></div><div class="svc-title">PRINTING SERVICES</div><div class="svc-text">Sed ut perspiciatis unde omnis iste natus error sit luptatem accusantium dol oremque laudan</div></div>
  </div>
  <a class="btn" href="#" style="top:505px;left:497px;width:207px;height:66px">READ MORE</a>
</section>

<!-- team -->
<h2 class="abs h2" style="top:2528px">MEET OUR <span class="red">TEAM</span></h2>
<div class="member" style="left:76px"><div class="ph" role="img" aria-label="Portrait of a smiling team member"></div><div class="nm">Name Heading</div></div>
<div class="member" style="left:346px"><div class="ph" role="img" aria-label="Portrait of a team member in a blazer"></div><div class="nm">Name Heading</div></div>
<div class="member" style="left:616px"><div class="ph" role="img" aria-label="Portrait of a team member in a grey sweater"></div><div class="nm">Name Heading</div></div>
<div class="member" style="left:886px"><div class="ph" role="img" aria-label="Portrait of a team member holding a tablet"></div><div class="nm">Name Heading</div></div>
<a class="btn" href="#" style="top:3042px;left:497px;width:207px;height:66px">READ MORE</a>

<!-- quote -->
<section class="quote abs">
  <p>“ Sed ut perspiciatis unde omnis iste natus error sit voluptatem accusantium doloremque laudantium, totam rem aperiam, eaque ipsa quae ab illo inventore veritatis.”</p>
  <div class="who">Name Heading</div>
</section>

<!-- blogs -->
<h2 class="abs h2" style="top:3726px;color:#2c3a45">BLOGS</h2>
<article class="post" style="left:76px"><div class="ph" style="background:linear-gradient(150deg,#6a6d74,#2f3035)" role="img" aria-label="Photo of a sealed envelope tied with twine"></div><div class="tt">Nemo enim ipsam voluptatem quia voluptas</div><a class="more" href="#">Read More</a></article>
<article class="post" style="left:435px"><div class="ph" style="background:linear-gradient(150deg,#7a8a72,#1d1d1f)" role="img" aria-label="Photo of a black mailbox in front of a house"></div><div class="tt">Nemo enim ipsam voluptatem quia voluptas</div><a class="more" href="#">Read More</a></article>
<article class="post" style="left:797px"><div class="ph" style="background:linear-gradient(150deg,#d9d9d6,#4a4a4c)" role="img" aria-label="Photo of a technician at a large format printer"></div><div class="tt">Nemo enim ipsam voluptatem quia voluptas</div><a class="more" href="#">Read More</a></article>

<!-- cta -->
<section class="cta abs">
  <h2>GET STARTED WITH TANDEM<br>PARCEL, TODAY</h2>
  <a class="btn" href="#">CONTACT US</a>
</section>

<!-- footer -->
<footer>
  <div class="abs brand" style="top:4862px;left:72px">
    <span class="brand-mark" style="width:18px;height:18px"></span><span class="brand-name" style="font-size:19px;color:var(--ink)">TANDEMPARCEL</span>
  </div>
  <p class="abs foot" style="top:4905px;left:76px;font-size:13px;line-height:25px">Copyright © 2024 Company Name.<br>All Right Reserved</p>

  <div class="abs foot-h" style="top:4778px;left:448px">Contact</div>
  <p class="abs foot" style="top:4820px;left:448px;line-height:28px">418 Harbor Way #120,<br>Eastfield, WA 98012</p>
  <p class="abs foot" style="top:4886px;left:448px">1-800-555-0142</p>
  <p class="abs foot" style="top:4925px;left:448px">info@companyname.com</p>
  <div class="abs social" aria-label="Social links">
    <span></span><span></span><span></span><span></span><span></span>
  </div>

  <a class="foot-link" href="#" style="top:4782px;left:793px">Home</a>
  <a class="foot-link" href="#" style="top:4821px;left:793px">About</a>
  <a class="foot-link" href="#" style="top:4860px;left:793px">Services</a>
  <a class="foot-link" href="#" style="top:4899px;left:793px">Team</a>
  <a class="foot-link" href="#" style="top:4782px;left:972px">Blog</a>
  <a class="foot-link" href="#" style="top:4821px;left:972px">Contact Us</a>
</footer>

</body>
</html>
```